International Travel Technology R&D business needs a wordpress website

We are a start up team of initially 2 individuals but plan to grow our team quickly, we have deep experience in travel technology. Our goal is to provide next generation technology research and development on behalf of our clients who are leading players in the travel technology industry. Attached our logos.

Target Market(s)

Travel Technology companies

Industry/Entity Type

Travel Industry

Coding

Coded - Design and coding required

Font styles to use
Sans Serif

Requirements
Must have
• Make use of our logo and colour scheme in the attached. Has to have a sense of adventure/ stepping into the unknown but equally must convey a sense of professionalism , we are a safe pair of hands. Sample themes are in the attachment .
Nice to have
• We have identified a theme on layoutbazaar which we feel would be inspirational. We hahe attached them to help in the design as inspiration.
Should not have
• images of airplanes , hotels etc, we want to project a future image.

```html
<!DOCTYPE html>
<html lang="en">
<head>
<meta charset="utf-8">
<title>Novaroute Labs</title>
<link href="https://fonts.googleapis.com/css2?family=Lato:wght@400;700&family=Orbitron:wght@600;700&display=swap" rel="stylesheet">
<style>
:root{
  --green:#3db54a;
  --green-dark:#2a8f36;
  --green-ring:#2c9a39;
  --navy:#1f2a5c;
  --ink:#222;
  --text:#444;
  --muted:#777;
  --light:#f1f1f1;
  --line:#d6d6d6;
  --footer:#2b2b2b;
  --footer-deep:#1b1b1b;
  --white:#fff;
}
*{box-sizing:border-box;margin:0;padding:0}
html,body{width:1200px;height:2582px;overflow:hidden}
body{position:relative;font-family:'Lato',sans-serif;color:var(--text);background:var(--white)}
.abs{position:absolute}
.topline{left:0;top:0;width:1200px;height:5px;background:#333}
.brand{left:100px;top:30px;font:700 30px 'Lato',sans-serif;color:var(--navy);display:flex;align-items:center;gap:12px}
.brand-dot{width:34px;height:34px;border-radius:50%;background:var(--green)}
.contact-pill{left:714px;top:0;width:414px;height:31px;background:#333;border-radius:0 0 30px 30px;color:#fff;font-size:15px;display:flex;align-items:center;justify-content:space-around}
.socials{left:950px;top:56px;display:flex;gap:10px}
.socials span{width:32px;height:32px;border-radius:50%}
.nav{left:0;top:112px;width:1200px;height:41px;background:var(--green)}
.nav a{position:absolute;top:0;height:41px;line-height:41px;color:#fff;font-size:15px;text-decoration:none}
.nav a.active{background:var(--navy);padding:0 20px;left:100px}
.hero{left:0;top:153px;width:1200px;height:508px;
  background:
    radial-gradient(circle at 520px 230px,rgba(90,200,230,.55) 0,rgba(60,140,90,.35) 90px,rgba(0,0,0,0) 190px),
    radial-gradient(circle at 820px 200px,rgba(120,190,240,.35) 0,rgba(0,0,0,0) 220px),
    radial-gradient(ellipse at 560px 560px,rgba(230,235,240,.6) 0,rgba(0,0,0,0) 260px),
    linear-gradient(110deg,#e4e8ec 0%,#9aa6b2 22%,#4c5c70 42%,#1c2a3c 62%,#3a4858 82%,#8b939c 100%)}
.tagline{left:0;top:661px;width:1200px;height:48px;background:var(--green);color:#fff;font:700 25px 'Lato',sans-serif;text-align:center;line-height:48px}
.heading{font:700 34px 'Orbitron',sans-serif;color:var(--ink);letter-spacing:2px}
.heading b{color:var(--green);font-weight:700}
.para{font-size:13.5px;line-height:26px;color:var(--text)}
.btn{background:var(--green-dark);color:#fff;font-weight:700;font-size:13px;text-align:center;border-radius:2px}
.quote{left:759px;top:784px;width:343px;height:316px;border:1px solid var(--line)}
.quote-tab{left:792px;top:776px;width:279px;height:40px;background:var(--green);color:#fff;font-weight:700;font-size:17px;text-align:center;line-height:40px}
.field{left:778px;width:303px;background:#efefef;border:1px solid #d0d0d0;border-radius:3px;font-size:13px;padding:8px 10px;color:#555}
.services{left:0;top:1150px;width:1200px;height:446px;background:linear-gradient(#f6f6f6,#e6e6e6)}
.divider{height:3px;border-top:1px solid #999;border-bottom:1px solid #999}
.svc-circle{width:114px;height:114px;border-radius:50%;background:radial-gradient(circle at 50% 40%,#4cc45a,var(--green) 60%,#2e9e3b);border:5px solid var(--green-ring);box-shadow:0 0 0 4px #fff;display:flex;align-items:center;justify-content:center}
.svc-circle svg{display:block}
.svc-title{font-size:19px;font-weight:700;color:var(--green)}
.svc-text{font-size:13px;line-height:20px;width:320px}
.svc-more{font-size:13px;color:#222;margin-top:4px}
.date{width:48px;height:60px;text-align:center;color:#fff}
.date .d{background:#333;height:32px;line-height:32px;font-weight:700;font-size:17px}
.date .m{background:var(--green);height:28px;line-height:28px;font-size:13px}
.blog-title{font-weight:700;font-size:16px;color:var(--ink)}
.testimonial{left:637px;top:1727px;width:462px;height:135px;border:1px solid #ccc;border-radius:6px;background:#fff;padding:16px 16px 0 48px;font-size:12px;line-height:20px;font-style:italic}
.dots span{display:inline-block;width:18px;height:18px;border-radius:50%;background:#333;color:#fff;font-size:11px;text-align:center;line-height:18px;margin-right:4px}
.partners{left:0;top:2003px;width:1200px;height:258px;background:var(--light)}
.badge{top:2133px;width:143px;height:74px;border:1px solid #ccc;background:#f8f8f8;border-radius:3px}
.badge i{position:absolute;left:46px;top:12px;width:50px;height:50px;border-radius:50%;background:#555}
.footer{left:0;top:2261px;width:1200px;height:274px;background:var(--footer)}
.footer h4{font:700 17px 'Orbitron',sans-serif;color:#fff;letter-spacing:1px}
.footer .item{color:#ddd;font-size:13px}
.copy{left:0;top:2535px;width:1200px;height:47px;background:var(--footer-deep);color:#ddd;font-size:13px;text-align:center;line-height:47px}
</style>
</head>
<body>
<div class="abs topline"></div>
<div class="abs brand"><span class="brand-dot"></span>Novaroute Labs</div>
<div class="abs contact-pill"><span>✉ hello@novaroutelabs.com</span><span>☎ +81 555.010.2040</span></div>
<div class="abs socials"><span style="background:#3aa5dc"></span><span style="background:#1b5fa6"></span><span style="background:#d92b27"></span><span style="background:#dc3b2d"></span></div>

<nav class="abs nav">
  <a class="active" href="#">Home</a>
  <a href="#" style="left:210px">About Us</a>
  <a href="#" style="left:336px">Our Services</a>
  <a href="#" style="left:487px">Media</a>
  <a href="#" style="left:594px">Testimonials</a>
  <a href="#" style="left:744px">Our Partners</a>
  <a href="#" style="left:897px">Blog</a>
  <a href="#" style="left:990px">Contact Us</a>
</nav>

<div class="abs hero" role="img" aria-label="Hands holding a tablet with a glowing globe, world map chart, network of people and floating app icons"></div>
<div class="abs tagline">We Are Passionate About Travel Technology</div>

<h2 class="abs heading" style="left:100px;top:756px">ABOUT <b>US</b></h2>
<div class="abs divider" style="left:100px;top:812px;width:612px;border-color:#ddd"></div>
<p class="abs para" style="left:100px;top:835px;width:615px">Lorem ipsum dolor sit amet, consectetuer adipiscing elit, sed diam nonummy nibh euismod tincidunt ut laoreet dolore magna aliquam erat volutpat. Ut wisi enim ad minim veniam, quis nostrud exerci tation ullamcorper suscipit lobortis nisl ut aliquip ex ea commodo consequat. Duis autem vel eum iriure dolor in hendrerit in vulputate velit esse molestie consequat, vel illum dolore eu feugiat nulla facilisis at vero eros et accumsan et iusto odio dignissim qui blandit praesent luptatum zzril delenit augue duis dolore te feugait nulla facilisi. Lorem ipsum dolor sit amet, consectetuer adipiscing elit, sed diam nonummy nibh euismod tincidunt ut laoreet dolore magna aliquam erat volutpat. Ut wisi enim ad minim veniam, quis nostrud exerci tation ullamcorper suscipit lobortis nisl ut aliquip ex ea commodo.</p>
<div class="abs btn" style="left:100px;top:1064px;width:115px;height:33px;line-height:33px">Read More</div>

<div class="abs quote"></div>
<div class="abs quote-tab">Get A Free Quote</div>
<div class="abs field" style="top:842px;height:33px">Name</div>
<div class="abs field" style="top:888px;height:33px">Email</div>
<div class="abs field" style="top:935px;height:81px">Massage</div>
<div class="abs btn" style="left:778px;top:1038px;width:83px;height:33px;line-height:33px">Submit</div>

<section class="abs services"></section>
<h2 class="abs heading" style="left:0;top:1198px;width:1200px;text-align:center">OUR <b>SERVICES</b></h2>
<div class="abs divider" style="left:100px;top:1255px;width:1002px"></div>

<!-- team icon -->
<div class="abs svc-circle" style="left:456px;top:1281px">
  <svg width="60" height="56" viewBox="0 0 60 56" fill="#fff">
    <circle cx="30" cy="12" r="8"/>
    <circle cx="12" cy="18" r="6"/>
    <circle cx="48" cy="18" r="6"/>
    <path d="M20 26h20a4 4 0 0 1 4 4v16h-8v10h-12v-10h-8v-16a4 4 0 0 1 4-4z"/>
    <path d="M4 28h10v18h-4v6h-6a2 2 0 0 1-2-2v-19a3 3 0 0 1 2-3z"/>
    <path d="M56 28h-10v18h4v6h6a2 2 0 0 0 2-2v-19a3 3 0 0 0-2-3z"/>
  </svg>
</div>
<!-- travel icon: suitcase and arrow -->
<div class="abs svc-circle" style="left:611px;top:1281px">
  <svg width="60" height="56" viewBox="0 0 60 56" fill="none" stroke="#fff" stroke-width="4" stroke-linecap="round" stroke-linejoin="round">
    <rect x="6" y="22" width="28" height="28" rx="4" fill="#fff" stroke="none"/>
    <path d="M14 22v-6h12v6"/>
    <path d="M36 36l18-18"/>
    <path d="M42 18h12v12"/>
  </svg>
</div>
<!-- research icon: two gears -->
<div class="abs svc-circle" style="left:456px;top:1427px">
  <svg width="62" height="60" viewBox="0 0 62 60">
    <circle cx="24" cy="36" r="15" fill="none" stroke="#fff" stroke-width="8" stroke-dasharray="5.9 5.9"/>
    <circle cx="24" cy="36" r="14" fill="#fff"/>
    <circle cx="24" cy="36" r="6" fill="#3db54a"/>
    <circle cx="47" cy="15" r="9" fill="none" stroke="#fff" stroke-width="6" stroke-dasharray="4.7 4.7"/>
    <circle cx="47" cy="15" r="8.5" fill="#fff"/>
    <circle cx="47" cy="15" r="3.5" fill="#3db54a"/>
  </svg>
</div>
<!-- development icon: gear -->
<div class="abs svc-circle" style="left:611px;top:1427px">
  <svg width="60" height="60" viewBox="0 0 60 60">
    <circle cx="30" cy="30" r="21" fill="none" stroke="#fff" stroke-width="10" stroke-dasharray="8.2 8.3"/>
    <circle cx="30" cy="30" r="20" fill="#fff"/>
    <circle cx="30" cy="30" r="8" fill="#3db54a"/>
  </svg>
</div>

<div class="abs" style="left:100px;top:1288px;width:320px;text-align:right"><div class="svc-title">Consolidators</div><p class="svc-text">Lorem ipsum dolor sit amet, consectetuer adipiscing sed diam nonummy nibh euismod tincidunt umagna gdag aliquam erat volutpat. tincidunt ut laoreetfgf</p><div class="svc-more">Read More &gt;&gt;</div></div>
<div class="abs" style="left:100px;top:1431px;width:320px;text-align:right"><div class="svc-title">Technology Research</div><p class="svc-text">Lorem ipsum dolor sit amet, consectetuer adipiscing sed diam nonummy nibh euismod tincidunt umagna gdag aliquam erat volutpat. tincidunt ut laoreetfgf</p><div class="svc-more">Read More &gt;&gt;</div></div>
<div class="abs" style="left:780px;top:1288px;width:320px"><div class="svc-title">Travel Agencies</div><p class="svc-text">Lorem ipsum dolor sit amet, consectetuer adipiscing sed diam nonummy nibh euismod tincidunt umagna gdag aliquam erat volutpat. tincidunt ut laoreetfgf.</p><div class="svc-more">Read More &gt;&gt;</div></div>
<div class="abs" style="left:780px;top:1431px;width:320px"><div class="svc-title">Development</div><p class="svc-text">Lorem ipsum dolor sit amet, consectetuer adipiscing sed diam nonummy nibh euismod tincidunt umagna gdag aliquam erat volutpat. tincidunt ut laoreetfgf.</p><div class="svc-more">Read More &gt;&gt;</div></div>

<h2 class="abs heading" style="left:100px;top:1643px">LATEST <b>BLOG</b></h2>
<div class="abs" style="left:100px;top:1700px;width:442px;border-top:1px solid #ddd"></div>
<div class="abs date" style="left:100px;top:1734px"><div class="d">24</div><div class="m">AUG</div></div>
<div class="abs" style="left:162px;top:1732px;width:380px"><div class="blog-title">Lorem Ipsum Dolor Sit Amet</div><p style="font-size:13px;line-height:20px">Lorem ipsum dolor sit amet, sed diam nonummy nibh euismod tincidunt ut laoreet dolore. Sit amet, sed diam nonu</p></div>
<div class="abs" style="left:162px;top:1812px;width:370px;border-top:1px solid #ccc"></div>
<div class="abs date" style="left:100px;top:1830px"><div class="d">24</div><div class="m">AUG</div></div>
<div class="abs" style="left:162px;top:1828px;width:380px"><div class="blog-title">Lorem Ipsum Dolor Sit Amet</div><p style="font-size:13px;line-height:20px">Lorem ipsum dolor sit amet, sed diam nonummy nibh euismod tincidunt ut laoreet dolore. Sit amet, sed diam nonu</p></div>
<div class="abs btn" style="left:100px;top:1918px;width:100px;height:33px;line-height:33px">View All</div>
<div class="abs" style="left:582px;top:1680px;height:270px;border-left:1px solid #e3e3e3"></div>

<h2 class="abs heading" style="left:624px;top:1643px">CLIENT <b>TESTIMONIALS</b></h2>
<div class="abs" style="left:624px;top:1700px;width:476px;border-top:1px solid #ddd"></div>
<div class="abs testimonial"><span style="position:absolute;left:12px;top:4px;font-size:40px;color:#bbb;font-style:normal">“</span>Lorem ipsum dolor sit amet, sed diam nonummy nibh euismod tincidunt ut laoreet dolore. Lorem ipsum dolor sit amet, sed diam nonummy nibh euismod tincidunt ut laoreet dolore. Lorem ipsum dolor sit amet, sed diam nonummy nibh euismod tincidunt ut laoreet dolore.</div>
<div class="abs" role="img" aria-label="Client portrait" style="left:620px;top:1822px;width:108px;height:108px;border-radius:50%;background:linear-gradient(#c99a72,#7a4e33);border:3px solid #fff"></div>
<div class="abs" style="left:693px;top:1892px;width:40px;height:40px;border-radius:50%;background:#bbb;color:#fff;text-align:center;font-size:28px;line-height:46px">”</div>
<div class="abs" style="left:744px;top:1834px;font-size:15px;color:#222">Dana Brooks <span style="color:#999;margin:0 8px">|</span> Customer</div>
<div class="abs dots" style="left:940px;top:1916px"><span style="background:var(--green)">1</span><span>2</span><span>3</span><span>4</span></div>

<section class="abs partners"></section>
<h2 class="abs heading" style="left:0;top:2050px;width:1200px;text-align:center">OUR <b>PARTNERS</b></h2>
<div class="abs divider" style="left:100px;top:2104px;width:1002px"></div>
<div class="abs badge" style="left:100px"><i></i></div>
<div class="abs badge" style="left:270px"><i></i></div>
<div class="abs badge" style="left:442px"><i></i></div>
<div class="abs badge" style="left:613px"><i></i></div>
<div class="abs badge" style="left:785px"><i></i></div>
<div class="abs badge" style="left:957px"><i></i></div>

<footer class="abs footer"></footer>
<svg class="abs" style="left:0;top:2261px" width="440" height="274"><polygon points="0,0 439,0 362,274 0,274" fill="#3db54a"/></svg>
<div class="abs" style="left:100px;top:2350px;width:260px;font:700 30px 'Lato',sans-serif;color:#fff;display:flex;align-items:center;gap:10px;justify-content:center"><span style="width:26px;height:26px;border-radius:50%;background:#fff"></span>Novaroute Labs</div>
<div class="abs socials" style="left:155px;top:2454px"><span style="background:#3aa5dc;width:28px;height:28px"></span><span style="background:#1b5fa6;width:28px;height:28px"></span><span style="background:#d92b27;width:28px;height:28px"></span><span style="background:#dc3b2d;width:28px;height:28px"></span></div>

<div class="abs footer" style="background:none;left:482px;top:2302px;width:320px;height:auto">
  <h4>CONTACT ADDRESS</h4>
  <div class="item" style="margin-top:20px;padding-left:22px;line-height:20px;position:relative"><svg style="position:absolute;left:0;top:3px" width="12" height="16"><path d="M6 0a6 6 0 0 1 6 6c0 4-6 10-6 10S0 10 0 6a6 6 0 0 1 6-6z" fill="#fff"/></svg>Lorem ipsum dolor sitamet, consectetuer adipiscing sed diam nonummy.</div>
  <div class="item" style="margin-top:12px;padding-left:22px">☎ &nbsp;555.010.2040</div>
  <div class="item" style="margin-top:12px;padding-left:22px">⎙ &nbsp;555.010.2040</div>
  <div class="item" style="margin-top:12px;padding-left:22px">✉ &nbsp;hello@novaroutelabs.com</div>
</div>
<div class="abs footer" style="background:none;left:839px;top:2302px;width:300px;height:auto">
  <h4>QUICK LINKS</h4>
</div>
<div class="abs item" style="left:839px;top:2348px;color:#ddd;font-size:13px;line-height:33px">› &nbsp;Home<br>› &nbsp;About Us<br>› &nbsp;Our Services<br>› &nbsp;Media<br>› &nbsp;Testimonials</div>
<div class="abs item" style="left:973px;top:2348px;color:#ddd;font-size:13px;line-height:33px">› &nbsp;Our Partners<br>› &nbsp;Blog<br>› &nbsp;Contact Us</div>

<div class="abs copy">Copyright © 2016 Novaroute Labs . All Right Reserved.</div>
<svg class="abs" style="left:100px;top:2535px" width="96" height="47"><polygon points="14,0 96,0 84,47 0,47" fill="#2f2f2f"/><polyline points="38,30 48,20 58,30" fill="none" stroke="#fff" stroke-width="3"/></svg>
</body>
</html>
```